Flyer for Makeup Class

A flyer for my makeup class promotion. I am a make up artist starting a group class to teach makeup to ladies. I have attached some verbiage handwritten. My picture is the one in pink hijab. I have also attached some inspiration ideas and color combination (the colors in the cake design are the ones I want to use).

Target Market(s)

Ladies looking to learn make up from a make up artist

Industry/Entity Type

Hair And Beauty

Requirements
Must have
• The verbiage / description that I have hand written should be written using graphics and nice fonts. You can change the exact wording to make it better.

```html
<!DOCTYPE html>
<html lang="en">
<head>
<meta charset="utf-8">
<title>Exclusive Makeup Masterclass</title>
<link href="https://fonts.googleapis.com/css2?family=Tenor+Sans&family=Oswald:wght@300;400&family=Lato:wght@300&display=swap" rel="stylesheet">
<style>
  :root {
    --cream: #f3ede4;
    --cream-light: #fbf8f4;
    --white: #ffffff;
    --ink: #1c1a19;
    --text: #4a4543;
    --gold: #b8956e;
    --rose: #d98c93;
    --blush: #f3c1b8;
    --hijab-top: #f6c9bd;
    --hijab-low: #f2b8ab;
    --magenta: #d8357f;
  }
  * { margin: 0; padding: 0; box-sizing: border-box; }
  html, body { width: 1014px; height: 1200px; overflow: hidden; background: var(--cream); }
  .flyer {
    position: relative; width: 1014px; height: 1200px; overflow: hidden;
    background:
      radial-gradient(ellipse 70% 35% at 50% 20%, var(--cream) 0%, transparent 80%),
      linear-gradient(180deg, #eee5d8 0%, var(--cream-light) 40%, var(--white) 55%, #f1ebe2 80%, #ebe2d5 100%);
  }
  .art { position: absolute; }
  .art--powder-top-left {
    left: -140px; top: -140px; width: 520px; height: 520px;
    background: radial-gradient(closest-side, rgba(190,80,95,.7) 0%, rgba(217,140,147,.5) 45%, rgba(243,193,184,.2) 75%, rgba(243,193,184,0) 100%);
  }
  .art--stroke-top-right {
    left: 770px; top: -90px; width: 340px; height: 330px;
    background: radial-gradient(closest-side, rgba(225,120,135,.65) 0%, rgba(243,170,175,.4) 50%, rgba(243,170,175,0) 100%);
  }
  .art--palette-bottom-right {
    left: 640px; top: 870px; width: 480px; height: 440px;
    background: radial-gradient(closest-side, rgba(199,122,90,.75) 0%, rgba(225,140,140,.55) 45%, rgba(243,193,184,.2) 78%, rgba(243,193,184,0) 100%);
  }
  .art--portrait { left: 0; top: 660px; width: 600px; height: 540px; }
  .header { position: absolute; top: 0; left: 0; width: 100%; text-align: center; }
  .header__kicker {
    position: absolute; top: 90px; width: 100%;
    font: 400 29px/1 "Tenor Sans", sans-serif; letter-spacing: 1px; color: var(--ink);
  }
  .header__title {
    position: absolute; top: 146px; width: 100%;
    font: 400 72px/1 "Tenor Sans", sans-serif; letter-spacing: 3px; color: var(--ink);
  }
  .header__host {
    position: absolute; top: 234px; width: 100%;
    font: 300 32px/1 "Oswald", sans-serif; letter-spacing: 7px; color: var(--gold);
  }
  .header__note {
    position: absolute; top: 290px; width: 100%;
    font: 300 18px/1 "Oswald", sans-serif; letter-spacing: 4px; color: var(--text);
  }
  .event-details {
    position: absolute; left: 39px; top: 363px; width: 931px; height: 86px;
    border: 2px solid var(--gold); display: flex; align-items: center; justify-content: center;
    font: 300 29px/1 "Oswald", sans-serif; letter-spacing: 1px; color: var(--ink);
  }
  .event-details__divider { margin: 0 14px; }
  .description {
    position: absolute; left: 60px; top: 471px; width: 894px; text-align: center;
    font: 300 28px/40px "Lato", sans-serif; color: var(--text);
  }
  .audience-ribbon { position: absolute; left: 129px; top: 593px; width: 764px; height: 43px; }
  .audience-ribbon svg { position: absolute; inset: 0; }
  .audience-ribbon__text {
    position: absolute; inset: 0; display: flex; align-items: center; justify-content: center;
    font: 300 19px/1 "Oswald", sans-serif; letter-spacing: 4px; color: var(--white);
  }
  .booking { position: absolute; left: 514px; top: 845px; }
  .booking__heading {
    font: 400 34px/1 "Oswald", sans-serif; letter-spacing: 2px; color: var(--gold);
    margin-bottom: 31px; white-space: nowrap;
  }
  .booking__item {
    display: flex; align-items: center; gap: 17px; height: 48px;
    font: 300 30px/1 "Lato", sans-serif; color: var(--text);
  }
  .booking__icon {
    width: 31px; height: 31px; border-radius: 50%; background: var(--gold);
    display: flex; align-items: center; justify-content: center; flex: none;
  }
</style>
</head>
<body>
<main class="flyer">
  <div class="art art--powder-top-left" role="img" aria-label="Crushed rose and bronze makeup powder"></div>
  <div class="art art--stroke-top-right" role="img" aria-label="Pink blush brush stroke"></div>
  <div class="art art--palette-bottom-right" role="img" aria-label="Pressed eyeshadow and blush pans in rose and terracotta"></div>
  <svg class="art art--portrait" width="600" height="540" viewBox="0 0 600 540" role="img" aria-label="Portrait of the makeup artist wearing a pink hijab">
    <defs>
      <linearGradient id="portraitTone" x1="0" y1="0" x2="0" y2="1">
        <stop offset="0" stop-color="var(--hijab-top)"/>
        <stop offset="0.7" stop-color="var(--hijab-low)"/>
        <stop offset="1" stop-color="var(--magenta)"/>
      </linearGradient>
    </defs>
    <path d="M0,540 L0,250 C20,110 90,22 200,20 C320,20 385,100 392,240 L398,400 C470,420 545,460 585,540 Z" fill="url(#portraitTone)"/>
  </svg>

  <header class="header">
    <p class="header__kicker">EXCLUSIVE MAKEUP</p>
    <h1 class="header__title">MASTERCLASS</h1>
    <p class="header__host">BY SAMIRA HADDAD</p>
    <p class="header__note">(UK BASED MUA)</p>
  </header>

  <div class="event-details">
    <span>ROSEWOOD CLUB GARDEN HALL (ISLAMABAD)</span>
    <span class="event-details__divider">|</span>
    <span>6TH APRIL 11:30 - 5:30PM</span>
  </div>

  <p class="description">This Class is packed with loads of information tips, live demos, goodie bag, certificate, Q &amp; A, Lunch and much more...</p>

  <div class="audience-ribbon">
    <svg width="764" height="43" viewBox="0 0 764 43" aria-hidden="true">
      <polygon points="0,0 764,0 750,21.5 764,43 0,43 14,21.5" fill="var(--gold)"/>
    </svg>
    <p class="audience-ribbon__text">PERFECT FOR PROFESSIONALS, BEGGINNERS &amp; MACKEUP LOVERS</p>
  </div>

  <section class="booking">
    <h2 class="booking__heading">TO BOOK YOUR PLACE CONTACT</h2>
    <p class="booking__item">
      <span class="booking__icon">
        <svg width="17" height="17" viewBox="0 0 24 24" aria-hidden="true"><path fill="#fff" d="M6.6 10.8a15.1 15.1 0 0 0 6.6 6.6l2.2-2.2c.3-.3.7-.4 1-.2 1.1.4 2.3.6 3.6.6.6 0 1 .4 1 1V20c0 .6-.4 1-1 1A17 17 0 0 1 3 4c0-.6.4-1 1-1h3.5c.6 0 1 .4 1 1 0 1.3.2 2.5.6 3.6.1.3 0 .7-.2 1z"/></svg>
      </span>
      071-555-0148
    </p>
    <p class="booking__item">
      <span class="booking__icon">
        <svg width="17" height="17" viewBox="0 0 24 24" aria-hidden="true"><path fill="#fff" d="M6.6 10.8a15.1 15.1 0 0 0 6.6 6.6l2.2-2.2c.3-.3.7-.4 1-.2 1.1.4 2.3.6 3.6.6.6 0 1 .4 1 1V20c0 .6-.4 1-1 1A17 17 0 0 1 3 4c0-.6.4-1 1-1h3.5c.6 0 1 .4 1 1 0 1.3.2 2.5.6 3.6.1.3 0 .7-.2 1z"/></svg>
      </span>
      03005550172
    </p>
    <p class="booking__item">
      <span class="booking__icon"></span>
      @samirahaddadmua
    </p>
  </section>
</main>
</body>
</html>
```